Organic Soap Packaging

We need a package design for a new company called Willow Naturals. Our primary product is organic soap. Our business model is based on the social entrepreneurial concept of by one give one like Brend shoes. We are giving soap to help prevent the spread of disease; 1.4 million deaths a year can be prevented by hand washing.

The design is for a recycled cardboard box/package. We want to demonstrate the high end, luxury feel of the product with undertones of organic/earth friendly/social conscious.

The soap is small batch, spa like, essential oil scented all natural luxury.
Updates

I am very excited about this startup business and I believe we will have great success! I am passionate about organic personal care and helping others in need. If you share my passion, please bring your work to the table!

Target Market(s)

My target market is people who are educated through college. Health conscious, socially conscious, Generation X. Basically shoppers of Green Basket and Haverline.

Industry/Entity Type

Business

Requirements
Must have
• Suitable for Face, Hair, and Skin
Scented with Organic Essential Oils

```html
<!DOCTYPE html>
<html lang="en">
<head>
<meta charset="utf-8">
<title>Willow Naturals – Soap Box Packaging</title>
<link rel="stylesheet" href="https://fonts.googleapis.com/css2?family=EB+Garamond:ital@0;1&family=Gochi+Hand&display=swap">
<style>
  :root{
    --mustard:#dcb443;
    --leaf:#3d6428;
    --kraft:#dfb283;
    --dieline:#a07a1f;
    --paper:#ffffff;
    --ink:#3a3318;
    --serif:"EB Garamond", Georgia, serif;
    --hand:"Gochi Hand", "Comic Sans MS", cursive;
  }
  *{box-sizing:border-box;margin:0;padding:0}
  html,body{width:1200px;height:1000px;overflow:hidden;background:var(--paper)}
  .canvas{position:relative;width:1200px;height:1000px;overflow:hidden;background:var(--paper)}
  .kraft-board{position:absolute;left:0;top:397px;width:1200px;height:603px;background:var(--kraft)}
  .dieline{position:absolute;left:0;top:0;width:1200px;height:1000px}
  .dieline path{fill:none;stroke:var(--dieline);stroke-width:1.3}

  .panel{position:absolute;background:var(--mustard);overflow:hidden}
  .card{box-shadow:0 3px 10px rgba(0,0,0,.35)}
  .front-card{left:132px;top:142px;width:383px;height:271px}
  .back-card{left:685px;top:142px;width:387px;height:271px}

  .band{position:absolute;background:var(--leaf);overflow:hidden;color:#fff;font-family:var(--serif);font-size:14px;white-space:nowrap}
  .band .buy{font-family:var(--hand);font-size:17px;margin-right:4px}
  .band-inner{position:absolute;display:flex;align-items:center}
  .front-card .band{left:0;top:0;width:45px;height:271px}
  .front-card .band-inner{width:271px;height:45px;left:-113px;top:113px;transform:rotate(-90deg);padding-left:14px}
  .back-card .band{right:0;top:0;width:49px;height:271px}
  .back-card .band-inner{width:271px;height:49px;left:-111px;top:111px;transform:rotate(90deg);justify-content:flex-end;padding-right:24px}

  .title{position:absolute;font-family:var(--hand);color:var(--leaf);text-align:center;line-height:.98}
  .title span{display:block}
  .t1{font-size:22px}.t2{font-size:21px}.t3{font-size:20px}.t4{font-size:18px}.t5{font-size:17px}.t6{font-size:16px}.t7{font-size:13px}
  .leaves{position:absolute;background:linear-gradient(90deg,rgba(61,100,40,.15),rgba(61,100,40,.55),rgba(61,100,40,.15));border-radius:40% 40% 10% 10%}
  .wave{position:absolute}
  .wave path{fill:none;stroke:var(--leaf);stroke-width:3.2;stroke-linecap:round}
  .suitable{position:absolute;font-family:var(--serif);color:var(--leaf);font-size:13px;white-space:nowrap}
  .crafted{position:absolute;font-family:var(--serif);font-style:italic;color:var(--leaf);font-size:12px;white-space:nowrap}
  .brand-name{position:absolute;font-family:var(--hand);color:var(--leaf);font-size:17px;white-space:nowrap}
  .brand-mark{position:absolute;width:28px;height:28px;background:var(--leaf)}
  .hand-icon{position:absolute;width:40px;height:36px;border-radius:50%;background:radial-gradient(circle,var(--leaf) 35%,rgba(61,100,40,.35) 70%,transparent 72%)}

  .facts{position:absolute;font-family:var(--serif);color:var(--ink);font-size:11.4px;line-height:14.6px}

  .front-card .title{left:255px;top:16px;width:120px}
  .front-card .leaves{left:253px;top:154px;width:120px;height:30px}
  .front-card .wave{left:45px;top:176px}
  .front-card .suitable{left:107px;top:192px}
  .front-card .crafted{left:136px;top:220px}
  .front-card .brand-name{left:190px;top:236px}
  .front-card .brand-mark{left:320px;top:224px}
  .back-card .facts{left:32px;top:10px;width:300px}
  .back-card .hand-icon{left:296px;top:226px}

  .box-panel{left:187px;top:560px;width:840px;height:388px}
  .box-panel .band{left:0;top:13px;width:840px;height:35px;display:flex;align-items:center;justify-content:flex-end;padding-right:26px}
  .box-panel .hand-icon{left:790px;top:46px}
  .front-face{position:absolute;left:128px;top:100px;width:310px;height:260px;transform:rotate(90deg)}
  .front-face .title{left:180px;top:0;width:110px}
  .front-face .title .t1{font-size:21px}
  .front-face .leaves{left:190px;top:124px;width:110px;height:30px}
  .front-face .wave{left:-20px;top:160px}
  .front-face .suitable{left:36px;top:176px}
  .front-face .crafted{left:80px;top:204px}
  .front-face .brand-name{left:140px;top:220px}
  .front-face .brand-mark{left:256px;top:214px}
  .facts-face{position:absolute;left:563px;top:110px;width:260px;height:240px;transform:rotate(-90deg)}
  .facts-face .facts{left:0;top:0;width:262px;font-size:11px;line-height:15.6px}
</style>
</head>
<body>
<div class="canvas">
  <div class="kraft-board"></div>

  <svg class="dieline" viewBox="0 0 1200 1000" aria-hidden="true">
    <path d="M187 1000 V520 H218 V440 Q218 427 232 427 H337 V543"/>
    <path d="M607 543 V427 H716 Q724 427 728 436 L740 458 V520 H757 V397"/>
    <path d="M187 543 H1027 M757 520 V543"/>
    <path d="M1027 543 L1100 563 V945 L1027 965"/>
    <path d="M187 965 H1027 M337 965 V1000 M607 965 V1000 M757 965 V1000"/>
  </svg>

  <!-- Front panel -->
  <section class="panel card front-card">
    <div class="band"><div class="band-inner"><span class="buy">Buy 1 Give 1</span>&nbsp;and help us prevent the spread of disease; 1.4 million deaths a year</div></div>
    <h1 class="title"><span class="t1">Luxury</span><span class="t2">Organic</span><span class="t3">Soap</span><span class="t4">scented</span><span class="t5">with</span><span class="t6">Essential</span><span class="t7">Oils</span></h1>
    <div class="leaves" role="img" aria-label="Hand-drawn leaf sprigs"></div>
    <svg class="wave" width="330" height="14" viewBox="0 0 330 14"><path d="M0 8 C60 12 100 4 160 7 S260 10 328 4"/></svg>
    <p class="suitable">This product is suitable for Face, Hair and Body.</p>
    <p class="crafted">Passionately handcrafted for you by:</p>
    <p class="brand-name">Willow Naturals</p>
    <div class="brand-mark"></div>
  </section>

  <!-- Back panel -->
  <section class="panel card back-card">
    <div class="facts">
      DID YOU KNOW?<br>
      - Sickness absence costs employers £495 a year in direct costs for every worker employed. Indirect costs are probably considerably more (WHC 2005 statistics)<br>
      - Norovirus – a common form of sickness and diarrhoea can result in individuals being off work for up to four days<br>
      - Handwashing is the best way to avoid colds, flu and other viruses (Professor Alan Brierly, of London's Kingsgate School of Medicine, and various others)<br>
      - Up to half of all men and a quarter of women fail to wash their hands after they've been to the toilet<br>
      - We have between 2 and 10 million bacteria between fingertip and elbow<br>
      - The number of germs on your fingertips doubles after you use the toilet<br>
      - Germs can stay alive on hands for up to three hours
    </div>
    <div class="hand-icon" role="img" aria-label="Hand and sun illustration"></div>
    <div class="band"><div class="band-inner">and help us prevent the spread of disease; 1.4 million deaths a year can be prevented by hand washing.</div></div>
  </section>

  <!-- Flat dieline main panel -->
  <section class="panel box-panel">
    <div class="band"><span class="buy">Buy 1 Give 1</span>&nbsp;and help us prevent the spread of disease; 1.4 million deaths a year can be prevented by hand washing.</div>
    <div class="hand-icon" role="img" aria-label="Hand and sun illustration"></div>

    <div class="front-face">
      <h2 class="title"><span class="t1">Luxury</span><span class="t2">Organic</span><span class="t3">Soap</span><span class="t4">scented</span><span class="t5">with</span><span class="t6">Essential</span><span class="t7">Oils</span></h2>
      <div class="leaves" role="img" aria-label="Hand-drawn leaf sprigs"></div>
      <svg class="wave" width="330" height="14" viewBox="0 0 330 14"><path d="M0 8 C60 12 100 4 160 7 S260 10 328 4"/></svg>
      <p class="suitable">This product is suitable for Face, Hair and Body.</p>
      <p class="crafted">Passionately handcrafted for you by:</p>
      <p class="brand-name">Willow Naturals</p>
      <div class="brand-mark"></div>
    </div>

    <div class="facts-face">
      <div class="facts">
        DID YOU KNOW?<br>
        - Sickness absence costs employers £495 a year in direct costs for every worker employed. Indirect costs are probably considerably more (WHC 2005 statistics)<br>
        - Norovirus – a common form of sickness and diarrhoea can result in individuals being off work for up to four days<br>
        - Handwashing is the best way to avoid colds, flu and other viruses (Professor Alan Brierly, of London's Kingsgate School of Medicine, and various others)<br>
        - Up to half of all men and a quarter of women fail to wash their hands after they've been to the toilet<br>
        - We have between 2 and 10 million bacteria between fingertip and elbow<br>
        - The number of germs on your fingertips doubles after you use the toilet<br>
        - Germs can stay alive on hands for up to three hours
      </div>
    </div>
  </section>
</div>
</body>
</html>
```